Mental Health

QRT HAVEN
Behavioral Health
4172 W. Pell St. Mesa, AZ 85219
Gwendolyn (480)555-0142 / Omar 480-555-0187

Email: QRTHaven@Mailvex.example
Newly Remodeled & Spacious
g Staff
Registered Nurses
Licensed Independent &
Professional Substance &
Abuse Counselors
Behavioral Health Techs
Certified Caregivers
Behavioral Health &
Substance Abuse Professionals

To Refer a Patient
About Us
QRT Haven is a Fully Staffed Behavioral
Health Residential Facility, providing
treatment plans for adults suffering
with various Behavioral Health and
Substance Abuse disorders, while living
in a nice safe, clean and supportive
environment. Our home offers clients the
ability to learn the necessary skills to
help clients adapt, build self confidence
as well as independence, with the goal
of reducing the probability of a future
crisis or possible relapse. We offer
counseling programs, consisting of a
variety of addiction and recovery support
groups, independent living, coping and
social skills groups, as well as assisting
clients with using tools to create a resume
to help obtain employment and so much
more. We are committed to teaching
self management care and allowing
clients to understand how to utilize the
resources, skills and tools available for
long term success by providing superior
quality, all-inclusive living arrangements
and treatment options.

Thank you for your patience while I update the final content needed for us to make the final decision this week.

```html
<!DOCTYPE html>
<html lang="en">
<head>
<meta charset="utf-8">
<title>QRT Haven Business Card</title>
<link href="https://fonts.googleapis.com/css2?family=Roboto:ital,wght@0,400;0,500;0,700;1,400;1,500&display=swap" rel="stylesheet">
<style>
  :root {
    --bg: #d9d9d9;
    --card-white: #ffffff;
    --brand-blue: #0a66c2;
    --brand-green: #6aa832;
    --brand-orange: #f06a1c;
    --card-dark: #2a2a2b;
    --text-light: #ffffff;
    --dot-red: #d8261f;
    --dot-orange: #f2a51c;
    --mark-grey: #4a4a4a;
  }
  * { margin: 0; padding: 0; box-sizing: border-box; }
  html, body {
    width: 1200px; height: 800px; overflow: hidden;
    background: var(--bg);
    font-family: "Roboto", Arial, sans-serif;
  }
  .canvas {
    width: 1200px; height: 800px;
    display: flex; align-items: center; justify-content: center; gap: 40px;
  }
  .card {
    position: relative;
    width: 560px; height: 320px;
    border-radius: 22px;
    overflow: hidden;
    box-shadow: 0 8px 24px rgba(0,0,0,0.18);
  }

  /* Front */
  .card--front { background: var(--card-white); }
  .card__wave { position: absolute; inset: 0; }
  .brand {
    position: absolute;
    display: flex; align-items: center; gap: 14px;
    color: var(--brand-blue);
    font-weight: 400;
    white-space: nowrap;
  }
  .brand__mark { border-radius: 50%; background: var(--mark-grey); flex: none; }
  .card--front .brand { left: 34px; top: 130px; font-size: 38px; }
  .card--front .brand__mark { width: 58px; height: 58px; }

  .contact {
    position: absolute;
    left: 340px; right: 10px; top: 36px;
    text-align: center;
    color: var(--text-light);
    line-height: 1.25;
  }
  .contact__name { font-size: 22px; font-weight: 700; letter-spacing: 0.5px; }
  .contact__phone { font-size: 14px; margin-bottom: 8px; }
  .contact__company { font-size: 13px; font-weight: 700; margin-top: 14px; }
  .contact__line { font-size: 13px; }

  /* Back */
  .card--back { background: var(--card-dark); }
  .card--back .brand {
    left: 50%; top: 70px; transform: translateX(-50%);
    font-size: 56px; gap: 20px;
  }
  .card--back .brand__mark { width: 96px; height: 96px; background: #5a5a5a; }
  .services {
    position: absolute; left: 0; right: 0; top: 218px;
    text-align: center; line-height: 1.3;
  }
  .services__lead { color: var(--brand-blue); font-weight: 700; font-size: 15px; }
  .services__team { color: var(--brand-green); font-style: italic; font-weight: 500; font-size: 14px; }
  .services__roles { color: var(--text-light); font-weight: 500; font-size: 11.5px; }
  .dot { display: inline-block; width: 6px; height: 6px; border-radius: 50%; margin: 0 4px; vertical-align: middle; }
  .dot--red { background: var(--dot-red); }
  .dot--orange { background: var(--dot-orange); }
</style>
</head>
<body>
<main class="canvas">
  <section class="card card--front" aria-label="Business card front">
    <svg class="card__wave" width="560" height="320" viewBox="0 0 560 320" aria-hidden="true">
      <path d="M250 0 C345 0 340 130 330 190 C320 262 360 320 440 320 L560 320 L560 0 Z" fill="var(--brand-blue)"/>
      <path d="M236 2 C330 6 328 130 318 190 C308 250 330 300 380 316" fill="none" stroke="var(--brand-orange)" stroke-width="4"/>
      <path d="M322 200 C312 262 352 314 430 318" fill="none" stroke="var(--brand-green)" stroke-width="4"/>
    </svg>
    <div class="brand">
      <span class="brand__mark"></span>
      <span class="brand__name">QRT Haven</span>
    </div>
    <div class="contact">
      <p class="contact__name">OMAR</p>
      <p class="contact__phone">480-555-0187</p>
      <p class="contact__name">GWENDOLYN</p>
      <p class="contact__phone">(480)555-0142</p>
      <p class="contact__company">QRT HAVEN Behavioral Health</p>
      <p class="contact__line">4172 W. Pell St. Mesa, AZ 85219</p>
      <p class="contact__line">QRTHaven@Mailvex.example</p>
    </div>
  </section>

  <section class="card card--back" aria-label="Business card back">
    <div class="brand">
      <span class="brand__mark"></span>
      <span class="brand__name">QRT Haven</span>
    </div>
    <div class="services">
      <p class="services__lead">Newly Remodeled &amp; Spacious Staff Registered Nurses</p>
      <p class="services__team">Licensed Independent &amp; Professional Substance &amp; Abuse Counselors</p>
      <p class="services__roles">Behavioral Health Techs<span class="dot dot--red"></span>Certified Caregivers<span class="dot dot--orange"></span>Behavioral Health &amp; Substance Abuse Professionals</p>
    </div>
  </section>
</main>
</body>
</html>
```